U.S. based testing, inspection, and certification (TIC) company needs a new social media design.

We need a social media design primarily for LinkedIn 1200x1200px for our U.S. based company with international capabilities for performing dozens if not hundreds of testing, inspection, and certification (TIC) services. Our primary services include calibration, chemical analysis, consulting engineering, environmental simulation, forensic engineering, materials testing, mechanical testing, and nondestructive testing. Industries we serve are aerospace/aviation, automotive, chemical, commercial properties, construction, consumer products, defense, energy storage, healthcare, insurance/legal, life science, manufacturing, oil & gas, power generation, pulp & paper, and telecommunications. https://veltrolabs.example/

Guideline hex colors (primary, secondary): #29aae2, #0b1f3b

The final design should communicate:
1. Trust, Integrity, and Independence
2. Technical Expertise and Accuracy
3. Efficiency and Speed
4. Value-Added Partnership

We previously used a hexagon design that we would like to part ways from; hexagon examples and KRV logos uploaded.

```html
<!DOCTYPE html>
<html lang="en">
<head>
<meta charset="UTF-8">
<title>KRV – From confidence to certainty</title>
<link href="https://fonts.googleapis.com/css2?family=Arimo:wght@400;700&family=Open+Sans:wght@600&family=Roboto+Condensed:wght@600&display=swap" rel="stylesheet">
<style>
  :root {
    --brand-sky: #29aae2;
    --brand-navy: #0b1f3b;
    --white: #ffffff;
    --space-deep: #02060f;
    --space-mid: #0a2a66;
    --horizon: #3f7fc8;
    --cloud: #b9cde6;
  }
  * { margin: 0; padding: 0; box-sizing: border-box; }
  html, body { width: 1200px; height: 1200px; overflow: hidden; background: var(--white); }
  .canvas { position: relative; width: 1200px; height: 1200px; overflow: hidden; background: var(--brand-sky); }

  .hero-image {
    position: absolute; left: 0; top: 0; width: 1200px; height: 742px;
    background:
      radial-gradient(ellipse 700px 260px at 900px 640px, var(--cloud) 0%, rgba(185,205,230,0.35) 40%, transparent 75%),
      radial-gradient(ellipse 1100px 500px at 850px 560px, var(--horizon) 0%, var(--space-mid) 45%, transparent 80%),
      linear-gradient(160deg, var(--space-deep) 0%, #061634 40%, var(--space-mid) 100%);
  }

  .brand { position: absolute; left: 344px; top: 52px; width: 416px; text-align: center; color: var(--white); font-family: "Arimo", Arial, sans-serif; }
  .brand-name { font-weight: 700; font-size: 150px; line-height: 150px; letter-spacing: 6px; }
  .brand-tagline { font-weight: 400; font-size: 33px; line-height: 40px; margin-top: -4px; white-space: nowrap; }

  .headline {
    position: absolute; left: 82px; top: 281px;
    font-family: "Arimo", Arial, sans-serif; font-weight: 700;
    font-size: 118px; line-height: 135px; color: var(--white); letter-spacing: -0.5px;
  }

  .section-label {
    position: absolute; left: 0; width: 424px; height: 50px;
    background: var(--brand-navy); color: var(--white);
    font-family: "Open Sans", Arial, sans-serif; font-weight: 600; font-size: 24px;
    line-height: 50px; padding-left: 77px;
  }
  .label-services { top: 780px; }
  .label-industries { top: 940px; }

  .section-body {
    position: absolute; left: 78px; width: 1090px;
    font-family: "Roboto Condensed", Arial, sans-serif; font-weight: 600;
    font-size: 27.5px; line-height: 35px; color: var(--white);
  }
  .body-services { top: 845px; }
  .body-industries { top: 998px; }

  .site-url {
    position: absolute; left: 78px; top: 1108px;
    font-family: "Arimo", Arial, sans-serif; font-weight: 700; font-size: 29px;
    color: var(--brand-navy);
  }
</style>
</head>
<body>
<main class="canvas">
  <div class="hero-image" role="img" aria-label="Photograph of a satellite with solar panels orbiting above Earth, clouds and blue horizon below"></div>

  <div class="brand">
    <div class="brand-name">KRV</div>
    <div class="brand-tagline">Veltro Technical Services</div>
  </div>

  <h1 class="headline">We take you from<br>confidence to<br>certainty</h1>

  <div class="section-label label-services">Our primary services</div>
  <p class="section-body body-services">calibration, chemical analysis, consulting engineering, environmental simulation, forensic engineering, materials testing, mechanical testing, and nondestructive testing.</p>

  <div class="section-label label-industries">Industries we serve</div>
  <p class="section-body body-industries">aerospace/aviation, automotive, chemical, commercial properties, construction, consumer products, defense, energy storage, healthcare, insurance/legal, life science, manufacturing, oil &amp; gas, power generation, pulp &amp; paper, and telecommunications.</p>

  <div class="site-url">https://veltrolabs.example/</div>
</main>
</body>
</html>
```